House Builder and Property Development Card Design and Logo

I need a business card design for a building and property development company.
Colour scheme of Dark Grey and Green, I would like it bold, sharp and professional.
No logo yet done, I'm open to options but please stay away from the usual- house, roof, hammers etc.
Thanks Rob

Please be aware that on the business card information section the WHRC # 5528391 is a licence number and my phone number 0492837165. The numbers are close together and could be mistaken as one whole number 

Thank you

                                   

Industry/Entity Type

Building

Contact Information for Business Card

VARGA BUILD & DEVELOPMENT.
Residential Building & Property Development
Robert Varga - Director
WHRC # 5528391
0492837165
rob@vargabuild.example.com.au

Requirements
Must have
• Bold Business name
Dark grey and green colours
Should not have
• roof outline or hammer logo

```html
<!DOCTYPE html>
<html lang="en">
<head>
<meta charset="utf-8">
<title>Varga Build &amp; Development – Business Card</title>
<link rel="stylesheet" href="https://fonts.googleapis.com/css2?family=PT+Sans:wght@400;700&display=swap">
<style>
  :root {
    --backdrop: #2a2b2d;
    --grey-dark: #6f757c;
    --grey-mid: #9aa0a6;
    --grey-light: #c9ccd0;
    --paper: #f4f5f6;
    --green: #1f8a5c;
    --green-deep: #0f3d2c;
    --text-light: #eef0f2;
  }
  * { box-sizing: border-box; margin: 0; padding: 0; }
  html, body {
    width: 1200px; height: 900px; overflow: hidden;
    background: var(--backdrop);
    font-family: "PT Sans", Arial, sans-serif;
  }
  .canvas { position: relative; width: 1200px; height: 900px; }

  .card {
    position: absolute; left: 280px; width: 640px; height: 366px;
    overflow: hidden; border-radius: 2px;
    box-shadow: 0 12px 30px rgba(0,0,0,.45);
  }
  .card--front { top: 48px; background: linear-gradient(160deg, var(--grey-light), var(--grey-mid) 55%, var(--grey-dark)); }
  .card--back  { top: 470px; background: linear-gradient(180deg, #ffffff 0%, var(--paper) 70%, #dfe1e4 100%); }

  .front-band { position: absolute; inset: 0; width: 100%; height: 100%; }

  .brand {
    position: absolute; left: 58px; top: 150px;
    display: flex; align-items: center; gap: 18px;
  }
  .brand__dot {
    width: 78px; height: 78px; border-radius: 50%;
    background: var(--green);
  }
  .brand__name {
    font-weight: 700; font-size: 40px; line-height: 1; letter-spacing: 1px;
    color: var(--green-deep);
  }
  .brand__name small { display: block; font-size: 17px; letter-spacing: 3px; margin-top: 6px; }

  .back-band {
    position: absolute; left: 0; right: 0; top: 112px; height: 140px;
    background: linear-gradient(90deg, var(--grey-dark), var(--grey-mid) 60%, #b4b8bd);
  }
  .contact {
    position: absolute; left: 44px; top: 132px; color: var(--text-light);
  }
  .contact__name { font-weight: 700; font-size: 17px; margin-bottom: 18px; }
  .contact__line { font-size: 13px; line-height: 1.4; color: #e2e5e8; }
  .divider {
    position: absolute; left: 372px; top: 122px; width: 1px; height: 120px;
    background: rgba(255,255,255,.8);
  }
  .back-mark {
    position: absolute; left: 445px; top: 100px; width: 160px; height: 160px;
    border-radius: 50%; background: var(--green);
    box-shadow: 0 14px 18px rgba(0,0,0,.25);
  }
</style>
</head>
<body>
<main class="canvas">
  <section class="card card--front" aria-label="Card front">
    <svg class="front-band" viewBox="0 0 640 366" preserveAspectRatio="none" aria-hidden="true">
      <polygon points="0,170 640,40 640,160 0,300" fill="#ffffff" opacity="0.95"/>
      <polygon points="0,300 640,160 640,175 0,315" fill="#e3e5e8"/>
    </svg>
    <div class="brand">
      <span class="brand__dot"></span>
      <p class="brand__name">VARGA<small>BUILD &amp; DEVELOPMENT</small></p>
    </div>
  </section>

  <section class="card card--back" aria-label="Card back">
    <div class="back-band"></div>
    <div class="contact">
      <p class="contact__name">Robert Varga - Director</p>
      <p class="contact__line">WHRC # 5528391</p>
      <p class="contact__line">Phone: 0492 837 165</p>
      <p class="contact__line">Email: rob@vargabuild.example.com.au</p>
    </div>
    <span class="divider"></span>
    <span class="back-mark"></span>
  </section>
</main>
</body>
</html>
```